電子書籍の表紙のデザイン案を募集致します。 電子書籍のテーマは投資で、主に初心者向けに 2024年から始まる新KOVUという制度の基本が学べる内容となっています。 親しみやすく、手にとりやすいデザインを希望しています。 タイトルは目立つようにし、「新KOVU」が目立つようにお願いします。 イラスト、写真など素材の使用は自由ですが、著作権違反の素材を使用しないようにだけご注意ください。 ■内容 ・タイトル、キャッチコピーを見て、自由にデザインしてください。 ・タイトル、キャッチコピー、著者名、レーベル名を表紙に入れてください。 ・サイズ:1600 x 2560 ・jpg形式での納品 ■必須事項 以下の4つの文言を入れてください 1・タイトル:目覚めるカイ・月光堂!真夏の夜に語りたい不思議な話! 2・キャッチコピー:静かなKOVUを選ぶ理由?週末に読める物語 3・著者名:木原沙都美 4・レーベル名:TAVEN BOOKS(ロゴを添付します) その他ご質問等ありましたら、気軽にお問い合わせください。 ご応募をお待ちしております! |
どの案も素敵でしたが、文字が印象的で勢いがあり、目立つこちらの案を採用させていただきました。
たくさんのご提案ありがとうございました。また機会がありましたらお声掛けさせていただくこともあるかと思いますので、今後ともどうぞよろしくお願いいたします。

```html
<!DOCTYPE html>
<html lang="ja">
<head>
<meta charset="utf-8">
<title>目覚めるカイ・月光堂 — 表紙</title>
<link rel="stylesheet" href="https://fonts.googleapis.com/css2?family=Noto+Serif+JP:wght@700;900&family=Noto+Sans+JP:wght@400;500;700&display=swap">
<style>
  :root {
    --ink: #000000;
    --paper: #ffffff;
    --accent: #f2d36b;
    --accent-deep: #e6c24e;
    --label-ink: #1a1a1a;
  }
  * { margin: 0; padding: 0; box-sizing: border-box; }
  html, body {
    width: 749px;
    height: 1200px;
    overflow: hidden;
    background: var(--ink);
  }
  .cover {
    position: relative;
    width: 749px;
    height: 1200px;
    background: var(--ink);
    color: var(--paper);
    font-family: "Noto Sans JP", sans-serif;
  }
  .kicker {
    position: absolute;
    left: 40px;
    top: 138px;
    font-family: "Noto Sans JP", sans-serif;
    font-weight: 500;
    font-size: 42px;
    letter-spacing: 1px;
  }
  .title {
    position: absolute;
    left: 0;
    right: 0;
    top: 214px;
    text-align: center;
    font-family: "Noto Serif JP", serif;
    font-weight: 900;
    font-size: 82px;
    line-height: 1.1;
    letter-spacing: 2px;
  }
  .title-rule {
    position: absolute;
    left: 106px;
    width: 530px;
    top: 314px;
    height: 10px;
    background: var(--accent);
  }
  .tagline {
    position: absolute;
    left: 0;
    right: 0;
    top: 352px;
    text-align: center;
    font-family: "Noto Serif JP", serif;
    font-weight: 700;
    font-size: 33px;
    line-height: 50px;
    color: var(--accent);
  }
  .emblem {
    position: absolute;
    left: 222px;
    top: 488px;
    width: 310px;
    height: 310px;
  }
  .subtitle {
    position: absolute;
    left: 96px;
    top: 900px;
    font-size: 30px;
    line-height: 48px;
    font-weight: 400;
    color: var(--paper);
  }
  .label-band {
    position: absolute;
    left: 0;
    right: 0;
    top: 1015px;
    height: 94px;
    background: var(--accent);
    color: var(--label-ink);
  }
  .imprint {
    position: absolute;
    left: 290px;
    width: 150px;
    top: 18px;
    text-align: center;
    font-weight: 700;
    font-size: 23px;
    line-height: 30px;
    letter-spacing: 1px;
  }
  .author {
    position: absolute;
    left: 560px;
    width: 180px;
    top: 30px;
    text-align: center;
    font-weight: 500;
    font-size: 22px;
    line-height: 32px;
  }
</style>
</head>
<body>
  <main class="cover">
    <p class="kicker">目覚める</p>
    <h1 class="title">カイ・月光堂</h1>
    <div class="title-rule"></div>
    <p class="tagline">真夏の夜に語りたい<br>不思議な話!</p>

    <svg class="emblem" viewBox="0 0 310 310" role="img" aria-label="上昇する矢印とコインのイラスト">
      <defs>
        <radialGradient id="emblem-fill" cx="50%" cy="50%" r="50%">
          <stop offset="0%" stop-color="#f2d36b" stop-opacity="0.55"/>
          <stop offset="100%" stop-color="#f2d36b" stop-opacity="0"/>
        </radialGradient>
      </defs>
      <rect width="310" height="310" fill="url(#emblem-fill)"/>
    </svg>

    <p class="subtitle">静かなKOVUを選ぶ理由?週末に<br>読める物語</p>

    <footer class="label-band">
      <p class="imprint">TAVEN<br>BOOKS</p>
      <p class="author">木原沙都美</p>
    </footer>
  </main>
</body>
</html>
```